A crooked lantern for Marisol Fenwick

I need a book cover for this novella to be published as an e-book. The design should be an illustration using graphic elements relating to the main themes: backwards time travel and a journey to India. The style should be quirky, eye-catching, intriguing, playful. I have attached some covers that I like as reference.

Target Market(s)

Fiction readers

Font styles to use
Decorative

Requirements
Must have
• Strong visual recognition when viewed as thumbnail image on Pellora etc
Nice to have
• Interesting typography
Should not have
• No obvious images of people or places in India. The Indian aspect should come across by use of colours or fonts or graphic design.

```html
<!DOCTYPE html>
<html lang="en">
<head>
<meta charset="utf-8">
<title>A Crooked Lantern – Cover Spread</title>
<link href="https://fonts.googleapis.com/css2?family=Great+Vibes&family=Montserrat:wght@700&display=swap" rel="stylesheet">
<style>
  :root{
    --page:#ffffff;
    --back-blue:#79e6ff;
    --spine-red:#ee3a48;
    --ink-black:#111111;
    --ink-brown:#4a3728;
    --white:#ffffff;
    --sky:#5cd0fb;
    --amber:#ffb70a;
    --orange:#ff7a1f;
    --sand:#f6d7b4;
  }
  *{margin:0;padding:0;box-sizing:border-box}
  html,body{width:1200px;height:1200px;overflow:hidden;background:var(--page)}
  .canvas{position:relative;width:1200px;height:1200px}

  .back-cover{position:absolute;left:72px;top:141px;width:491px;height:694px;background:var(--back-blue)}
  .back-title{position:absolute;left:0;top:42px;width:525px;text-align:center;
    font-family:"Great Vibes",cursive;font-weight:400;font-size:72px;line-height:62px;color:var(--ink-black)}
  .author-photo{position:absolute;left:58px;top:274px;width:118px;height:135px;background:var(--white)}
  .author-bio{position:absolute;left:202px;top:277px;font-family:"Montserrat",sans-serif;
    font-weight:700;font-size:11px;color:var(--ink-black)}
  .code-box{position:absolute;left:262px;top:564px;width:179px;height:97px;
    background:var(--white);border:1px solid var(--ink-black)}

  .spine{position:absolute;left:563px;top:141px;width:54px;height:694px;background:var(--spine-red);overflow:hidden}
  .spine-text{position:absolute;left:0;width:54px;display:flex;justify-content:center;
    writing-mode:vertical-rl;font-family:"Great Vibes",cursive;font-size:34px;line-height:54px;
    color:var(--white);white-space:nowrap}
  .spine-title{top:28px}
  .spine-author{top:418px}

  .front-cover{position:absolute;left:617px;top:141px;width:493px;height:694px;overflow:hidden}
  .front-art{position:absolute;inset:0}
  .front-author{position:absolute;left:0;top:38px;width:100%;text-align:center;
    font-family:"Great Vibes",cursive;font-size:58px;color:var(--ink-brown)}
  .front-title{position:absolute;left:0;width:100%;text-align:center;font-family:"Great Vibes",cursive}
  .front-title-small{top:345px;font-size:96px;color:var(--ink-black)}
  .front-title-main{top:450px;font-size:100px;line-height:100px;color:var(--ink-brown);
    text-shadow:
      3px 3px 0 var(--white),-3px -3px 0 var(--white),3px -3px 0 var(--white),-3px 3px 0 var(--white),
      0 4px 0 var(--white),0 -4px 0 var(--white),4px 0 0 var(--white),-4px 0 0 var(--white)}
</style>
</head>
<body>
<div class="canvas">
  <section class="back-cover">
    <h2 class="back-title">A<br>Crooked<br>Lantern</h2>
    <div class="author-photo"></div>
    <p class="author-bio">Author of this book ...</p>
    <div class="code-box"></div>
  </section>

  <section class="spine">
    <span class="spine-text spine-title">A Crooked Lantern</span>
    <span class="spine-text spine-author">Marisol Fenwick</span>
  </section>

  <section class="front-cover">
    <svg class="front-art" role="img" aria-label="Stylised illustration looking up a tall striped tower between orange and yellow buildings against a blue sky" width="493" height="694" viewBox="0 0 493 694">
      <defs>
        <linearGradient id="artSky" x1="0" y1="0" x2="0" y2="1">
          <stop offset="0" stop-color="#5cd0fb"/>
          <stop offset="0.35" stop-color="#79e6ff"/>
          <stop offset="0.55" stop-color="#ff7a1f"/>
          <stop offset="0.8" stop-color="#f6d7b4"/>
          <stop offset="1" stop-color="#fff4e6"/>
        </linearGradient>
        <linearGradient id="artSide" x1="0" y1="0" x2="1" y2="0">
          <stop offset="0" stop-color="#ffb70a" stop-opacity="0.55"/>
          <stop offset="0.5" stop-color="#ffb70a" stop-opacity="0"/>
          <stop offset="1" stop-color="#ff7a1f" stop-opacity="0.55"/>
        </linearGradient>
      </defs>
      <rect width="493" height="694" fill="url(#artSky)"/>
      <rect width="493" height="694" fill="url(#artSide)"/>
    </svg>
    <div class="front-author">Marisol Fenwick</div>
    <div class="front-title front-title-small">A</div>
    <div class="front-title front-title-main">Crooked<br>Lantern</div>
  </section>
</div>
</body>
</html>
```